Orbeo app design for cryptocurrency trading investment fund Vornexa

Vornexa is an investment fund that help investors with investing in cryptocurrencies such as Zentrix and Pallidor. We use our own trading platform to buy and sell crypto currencies on behalf of the investors. As an extra service we want to develop an Orbeo app for our investors. After logging in the Orbeo app they can get a real-time insight in the value of their portfolio. We have created wireframes of these pages in attached zip file. This zip file also contains the logo of Vornexa.

We need you to design a clean professional and fresh app design based on the wireframes. The app design should contain the corporate identity of Vornexa and thus the following color codes and font type must be used:

Color 1: 489e95
Color 2: 474646
Font type: Open Sans

login.png
The investor first has to login the app

home.png
The first page the investor sees after logging in.

account.png
In the account section the investor can change his login access details to the app

account_b.png
On this page he can change his password.

Coin page (added as separate file)
This is the page that shows up when you click on one of the coins.

Target Market(s)

Investors who invest the minimum amount of € 100.000

Industry/Entity Type

Tech

Requirements
Must have
• Professional modern design
Should not have
• cheap colourful creative look and feel.

```html
<!DOCTYPE html>
<html lang="en">
<head>
<meta charset="utf-8">
<title>Vornexa – Login</title>
<link href="https://fonts.googleapis.com/css2?family=Open+Sans:wght@400;600&display=swap" rel="stylesheet">
<style>
  :root {
    --brand-teal: #489e95;
    --brand-grey: #474646;
    --text-muted: #8a8a8a;
    --line: #ececec;
    --screen-bg: #ffffff;
    --page-bg: #dfe5e8;
    --status-ink: #222222;
  }
  * { box-sizing: border-box; margin: 0; padding: 0; }
  html, body {
    width: 1200px; height: 1097px; overflow: hidden;
    background: var(--page-bg);
    font-family: "Open Sans", sans-serif;
  }
  .screen {
    position: absolute; left: 330px; top: 68px;
    width: 540px; height: 960px;
    background: var(--screen-bg);
    color: var(--brand-grey);
  }
  .status-bar {
    position: absolute; top: 0; left: 0; right: 0; height: 36px;
    display: flex; align-items: center; justify-content: space-between;
    padding: 0 14px; font-size: 15px; color: var(--status-ink);
  }
  .status-bar .signal { display: flex; align-items: center; gap: 3px; }
  .status-bar .dot { width: 7px; height: 7px; border-radius: 50%; background: var(--status-ink); }
  .status-bar .dot.empty { background: none; border: 1px solid var(--status-ink); }
  .status-bar .carrier { margin: 0 4px 0 5px; }
  .status-bar .battery { display: flex; align-items: center; gap: 6px; }
  .battery-icon { width: 30px; height: 13px; border: 1px solid var(--status-ink); border-radius: 3px; padding: 1px; }
  .battery-icon span { display: block; width: 80%; height: 100%; background: var(--status-ink); border-radius: 1px; }

  .brand {
    position: absolute; top: 170px; left: 0; right: 0;
    display: flex; align-items: center; justify-content: center; gap: 14px;
  }
  .brand-dot { width: 26px; height: 26px; border-radius: 50%; background: var(--brand-teal); }
  .brand-name { font-size: 40px; font-weight: 600; color: var(--brand-teal); }

  .welcome {
    position: absolute; top: 362px; left: 0; right: 0;
    text-align: center; font-size: 27px; font-weight: 400;
    letter-spacing: 0.5px;
  }
  .login-form { position: absolute; top: 450px; left: 70px; right: 70px; }
  .field {
    position: relative; height: 66px;
    border-bottom: 1px solid var(--line);
    display: flex; align-items: center; justify-content: center;
    font-size: 17px; color: var(--brand-grey);
  }
  .field .help {
    position: absolute; right: 0; width: 24px; height: 24px;
    border: 1px solid #ccc; border-radius: 50%;
    font-size: 11px; display: flex; align-items: center; justify-content: center; color: #666;
  }
  .login-button {
    position: absolute; top: 660px; left: 40px; right: 40px; height: 68px;
    background: var(--brand-teal); color: #fff; border: none;
    font-family: "Open Sans", sans-serif; font-weight: 600; font-size: 19px;
    display: flex; align-items: center; justify-content: center;
  }
  .signup {
    position: absolute; top: 750px; left: 0; right: 0;
    text-align: center; font-size: 17px; color: var(--text-muted);
  }
  .signup a { color: var(--brand-teal); text-decoration: none; }
</style>
</head>
<body>
  <main class="screen">
    <div class="status-bar">
      <div class="signal">
        <span class="dot"></span><span class="dot"></span><span class="dot"></span>
        <span class="dot empty"></span><span class="dot empty"></span>
        <span class="carrier">Nelvo</span>
        <svg width="16" height="12" viewBox="0 0 16 12" aria-hidden="true">
          <path d="M1 4 A10 10 0 0 1 15 4" fill="none" stroke="#222" stroke-width="1.6"/>
          <path d="M4 7 A6 6 0 0 1 12 7" fill="none" stroke="#222" stroke-width="1.6"/>
          <circle cx="8" cy="10" r="1.5" fill="#222"/>
        </svg>
      </div>
      <div class="time">1:43 pm</div>
      <div class="battery">80% <div class="battery-icon"><span></span></div></div>
    </div>

    <div class="brand">
      <span class="brand-dot"></span>
      <span class="brand-name">Vornexa</span>
    </div>

    <h1 class="welcome">WELCOME TO VORNEXA</h1>

    <form class="login-form">
      <div class="field">EMAIL <span class="help">?</span></div>
      <div class="field">PASSWORD</div>
      <div class="field"></div>
    </form>

    <button class="login-button" type="button">LOGIN</button>

    <p class="signup">Dont have an account ? <a href="#">Sign up</a></p>
  </main>
</body>
</html>
```